Packaging design - PROTEIN BALLS

PACKAGING
The packaging is a round carton roll, size: Ø73x180 mm, mockup sample enclosed, The label on the carton roll should have a size of 225x178 mm (width x height)

PRODUCT
Chrunchy, cheesy PROTEIN BALLS (100% pure cheese) with a huge amount of protein (65%), a lot of calcium and very low carbogydrates (3%). Diameter about 1.5 cm.

DESIGN
Since our customers are very sporty people, runner, bodybuilder, etc. The design must fit to this sporty customer segment.

FILES
We need the open data for InDesign with all fonts and pictures. If there are licenses tu buy, we will do it.

SUMMARY
1. SNACK
• Crunchy cheese balls with a diameter of about 1.5cm
• 3 different flavors: "Swiss Alpine Salt", "Provencale" and "Hot Chili"
• High in Protein (65%) and Calcium (2%)
• Low in carbohydrates (3%)

2. PACKAGING
• Carton roll, size: Ø73x180 mm
• Background can be every color, but we think a black one will be high premium.
• Maybe different sports are represented in the background, maybe also cheese
• Be creative
• Label applied, size: 225x178 mm

3. DESIGN
• Product name = (Cheese) PROTEIN BALLS
• 3 different colors for the 3 flavors "Swiss Alpine Salt", "Provencale" and "Hot Chili"
• HighProtein, High Calcium and LowCarb must be pointed out on the front
• Swissness: Swiss made must be pointed out
• fresh and young design, most customers are sporty people, pumper with a strong body awareness

TARGET CUSTOMER
Our main customers are extremely sporty people, who work very hard on their muscles and fitness, most of them are runners, cross fitnesser, bodybuilders, etc We will launch the product in fitness centers, in supplement shops and we are planning to make some stories with sporty influencer.

Serif
Sans Serif

• Cheese, naturalness, healthy, PROTEIN balls, muscles, Swissness must showed on the product.

```html
<!DOCTYPE html>
<html lang="en">
<head>
<meta charset="utf-8">
<title>Protein Balls – Provencale Label</title>
<link rel="stylesheet" href="https://fonts.googleapis.com/css2?family=Bebas+Neue&family=Playball&family=Caveat:wght@500&family=Amatic+SC:wght@700&family=Roboto+Condensed:wght@400&family=Libre+Franklin:wght@400;700;900&display=swap">
<style>
  :root {
    --page: #ffffff;
    --label-edge: #e4e4e4;
    --chalk-dark: #333333;
    --chalk-mid: #454545;
    --white: #ffffff;
    --cheese-gold: #c9bc90;
    --herb-green: #7b9b3a;
    --herb-dark: #4f6e22;
    --swiss-red: #c8261f;
    --facts-black: #050505;
    --sport-grey: #7d7d7d;
  }
  * { margin: 0; padding: 0; box-sizing: border-box; }
  html, body { width: 1200px; height: 1200px; overflow: hidden; background: var(--page); }
  .canvas { position: relative; width: 1200px; height: 1200px; }

  .label {
    position: absolute; left: 120px; top: 183px; width: 933px; height: 727px;
    border: 3px solid var(--label-edge);
    background: radial-gradient(ellipse at 50% 45%, var(--chalk-mid) 0%, var(--chalk-dark) 80%);
    overflow: hidden;
  }
  .sketch { position: absolute; border-radius: 50%; }
  .sketch--lifter { left: 348px; top: 88px; width: 258px; height: 205px; background: radial-gradient(ellipse, rgba(170,170,170,.22), rgba(170,170,170,0) 70%); }
  .sketch--small { background: radial-gradient(ellipse, rgba(150,150,150,.2), rgba(150,150,150,0) 70%); }
  .sketch--herb { left: 560px; top: 530px; width: 100px; height: 92px; z-index: 1; background: radial-gradient(ellipse, #7fa83f 0%, #5d8228 55%, rgba(93,130,40,0) 72%); }

  .swiss-made { position: absolute; left: 406px; top: 44px; font: 22px/1 "Bebas Neue", sans-serif; letter-spacing: 2px; color: var(--white); }
  .swiss-flag { position: absolute; left: 523px; top: 36px; }

  .sport-word { position: absolute; left: 773px; top: 50px; font: 34px/1 "Bebas Neue", sans-serif; letter-spacing: 2px; color: var(--sport-grey); }

  .title-cheese { position: absolute; left: 0; width: 933px; top: 216px; text-align: center; font: 58px/1 "Playball", cursive; color: var(--cheese-gold); }
  .title-main { position: absolute; left: 0; width: 933px; text-align: center; font-family: "Bebas Neue", sans-serif; color: var(--white); letter-spacing: 3px; }
  .title-main--protein { top: 282px; font-size: 92px; line-height: 1; }
  .title-main--balls { top: 365px; font-size: 92px; line-height: 1; }
  .for-athletes { position: absolute; left: 0; width: 933px; top: 465px; text-align: center; font: 30px/1 "Bebas Neue", sans-serif; letter-spacing: 3px; color: var(--white); }

  .flavour-banner { position: absolute; left: 349px; top: 522px; width: 240px; height: 54px; background: var(--herb-green); border: 2px dotted #9dba5c; }
  .flavour-name { position: absolute; left: 349px; top: 522px; width: 240px; height: 54px; z-index: 2; text-align: center; font: 40px/54px "Playball", cursive; color: var(--white); white-space: nowrap; }

  .claims { position: absolute; top: 623px; left: 362px; display: flex; gap: 11px; }
  .claim { width: 64px; height: 64px; border-radius: 50%; display: flex; align-items: center; justify-content: center; text-align: center; font: 700 17px/0.95 "Amatic SC", sans-serif; }
  .claim--filled { background: var(--herb-green); color: var(--white); box-shadow: inset 0 0 0 3px var(--herb-green), inset 0 0 0 5px var(--white); }
  .claim--outline { background: var(--white); color: var(--herb-green); box-shadow: inset 0 0 0 3px var(--white), inset 0 0 0 4.5px var(--chalk-dark); }

  .facts { position: absolute; left: 62px; top: 352px; width: 213px; height: 318px; background: var(--facts-black); border: 2px solid var(--white); outline: 2px solid var(--facts-black); padding: 4px 4px 4px 5px; color: var(--white); font-family: "Libre Franklin", sans-serif; }
  .facts__title { font: 900 22px/1 "Libre Franklin", sans-serif; letter-spacing: 0.8px; padding-bottom: 3px; white-space: nowrap; }
  .facts__servings { font-size: 10.5px; }
  .facts__size { font-size: 11px; font-weight: 700; border-bottom: 5px solid var(--white); padding-bottom: 1px; }
  .facts__amount { font-size: 8.5px; font-weight: 700; margin-top: 1px; }
  .facts__calories { display: flex; justify-content: space-between; align-items: flex-end; font-weight: 900; border-bottom: 3px solid var(--white); line-height: 1; padding-bottom: 2px; }
  .facts__calories span:first-child { font-size: 18px; }
  .facts__calories span:last-child { font-size: 24px; }
  .facts__dv { text-align: right; font-size: 6.5px; font-weight: 700; padding: 2px 0 1px; border-bottom: 1px solid var(--white); }
  .facts__row { display: flex; justify-content: space-between; font-size: 8.6px; line-height: 12.4px; border-bottom: 1px solid #bbbbbb; }
  .facts__row b { font-weight: 700; }
  .facts__row--indent { padding-left: 12px; }
  .facts__row--indent2 { padding-left: 26px; }
  .facts__row--last { border-bottom: 5px solid var(--white); }
  .facts__note { font-size: 6px; line-height: 1.2; padding: 3px 0 3px; border-bottom: 1px solid #bbbbbb; }
  .facts__foot { font-size: 6px; line-height: 1.45; padding-top: 4px; }

  .description { position: absolute; left: 686px; top: 365px; width: 202px; text-align: center; font: 500 17px/0.9 "Caveat", cursive; color: var(--white); }
  .ingredients { position: absolute; left: 686px; top: 474px; font: 13.5px/1 "Roboto Condensed", sans-serif; color: var(--white); }
  .maker { position: absolute; left: 690px; top: 528px; font: 12px/1 "Roboto Condensed", sans-serif; color: var(--white); }
  .code-box { position: absolute; left: 685px; top: 608px; width: 207px; height: 74px; background: var(--white); }
</style>
</head>
<body>
<div class="canvas">
  <section class="label">
    <div class="sketch sketch--lifter" role="img" aria-label="Chalk sketch of an athlete lifting a dumbbell"></div>
    <div class="sketch sketch--small" style="left:40px;top:40px;width:110px;height:120px" role="img" aria-label="Chalk sketch of a tennis player and a football"></div>
    <div class="sketch sketch--small" style="left:120px;top:140px;width:150px;height:130px" role="img" aria-label="Chalk doodles of a start line, a barbell and a discus thrower"></div>
    <div class="sketch sketch--small" style="left:685px;top:70px;width:190px;height:130px" role="img" aria-label="Chalk sketch of a cyclist and a dumbbell"></div>
    <div class="sketch sketch--small" style="left:640px;top:220px;width:180px;height:130px" role="img" aria-label="Chalk doodles of a tennis racket, a ball and the word win"></div>
    <div class="sketch sketch--small" style="left:570px;top:400px;width:120px;height:120px" role="img" aria-label="Chalk sketch of a weightlifter"></div>
    <div class="sketch sketch--small" style="left:265px;top:585px;width:100px;height:110px" role="img" aria-label="Chalk sketch of a runner"></div>

    <div class="swiss-made">Swiss Made</div>
    <svg class="swiss-flag" width="46" height="38" viewBox="0 0 46 38" aria-hidden="true">
      <rect x="2" y="2" width="42" height="34" fill="var(--swiss-red)"/>
      <rect x="19" y="10" width="8" height="18" fill="var(--white)"/>
      <rect x="14" y="15" width="18" height="8" fill="var(--white)"/>
    </svg>
    <div class="sport-word">Sport</div>

    <div class="title-cheese">Cheese</div>
    <div class="title-main title-main--protein">Protein</div>
    <div class="title-main title-main--balls">Balls</div>
    <div class="for-athletes">- For Athletes -</div>

    <div class="flavour-banner"></div>
    <div class="sketch sketch--herb" role="img" aria-label="Illustrated sprig of basil leaves"></div>
    <div class="flavour-name">Provencale</div>

    <div class="claims">
      <div class="claim claim--filled">LOW<br>CARB</div>
      <div class="claim claim--outline">HIGH<br>PROTEIN<br>65%</div>
      <div class="claim claim--outline">HIGH<br>CALCIUM</div>
    </div>

    <div class="facts">
      <div class="facts__title">Nutrition Facts</div>
      <div class="facts__servings">8 servings per container</div>
      <div class="facts__size">Serving size</div>
      <div class="facts__amount">Amount Per Serving</div>
      <div class="facts__calories"><span>Calories</span><span>45</span></div>
      <div class="facts__dv">% Daily Value*</div>
      <div class="facts__row"><span><b>Total Fat</b> 4g</span><b>5%</b></div>
      <div class="facts__row facts__row--indent"><span>Saturated Fat 2.6g</span><b>13%</b></div>
      <div class="facts__row facts__row--indent"><span><i>Trans</i> Fat 0g</span><span></span></div>
      <div class="facts__row"><span><b>Cholesterol</b> 35mg</span><b>12%</b></div>
      <div class="facts__row"><span><b>Sodium</b> 45mg</span><b>2%</b></div>
      <div class="facts__row"><span><b>Total Carbohydrate</b> 1g</span><b>0%</b></div>
      <div class="facts__row facts__row--indent"><span>Dietary Fiber 0g</span><b>0%</b></div>
      <div class="facts__row facts__row--indent"><span>Total Sugars 0g</span><span></span></div>
      <div class="facts__row facts__row--indent2"><span>Includes 0g Added Sugars</span><b>0%</b></div>
      <div class="facts__row facts__row--last"><span><b>Protein</b> 2g</span><b>4%</b></div>
      <div class="facts__note">Not a significant source of vitamin D, calcium, iron, and potassium</div>
      <div class="facts__foot">*The % Daily Value (DV) tells you how much a nutrient in a serving of food contributes to a daily diet. 2,000 calories a day is used for general nutrition advice.</div>
    </div>

    <p class="description">Chrunchy, cheesy protein Balls (100% pure cheese) with a huge amount of protein (65%), a lot of calcium and very low carbogydrates (3%). Diameter about 1.5 cm.</p>
    <p class="ingredients">INGREDIENTS: 100% natural Cheese....</p>
    <p class="maker">Manufacture:<br>ALPKRUNCH<br>Address:<br>Switzerland<br>www.alpkrunch.example</p>
    <div class="code-box"></div>
  </section>
</div>
</body>
</html>
```